Flyer for a conference next week

We need a flyer to promote our stand at a conference next week - involving a jelly bean challenge.

The following files are attached:

- Existing Company Logos
- The logo of the product we are promoting (qTallon)
- A previous flyer - may be useful
- a Jellybean image (we want this to be the major part of the design

The flyer will be size : DL - 109mm x 220mm (5mm bleed) and 300 DPI

The flyer should include the following text :

"Take the Jelly Bean Challenge at the Velvet Orbit table in the exhibit space and win a Drone!"

"Find out more about our qTallon Web Services platform for Financial Models"

Colors
ed2e35

Requirements
Must have
• The flyer will be size : DL - 109mm x 220mm (5mm bleed) and 300 DPI
• The flyer should include the following text :
• "Take the Jelly Bean Challenge at the Velvet Orbit table in the exhibit space and win a Drone!"
• "Find out more about our qTallon Web Services platform for Financial Models"

```html
<!DOCTYPE html>
<html lang="en">
<head>
<meta charset="utf-8">
<title>Velvet Orbit – Jelly Bean Challenge Flyer</title>
<link href="https://fonts.googleapis.com/css2?family=Fredoka:wght@500;600&family=Black+Ops+One&display=swap" rel="stylesheet">
<style>
  :root {
    --red: #ed2e35;
    --red-deep: #d92329;
    --ink: #111111;
    --paper: #ffffff;
    --blush: #fdf0f1;
    --bean-warm: #e8463a;
    --bean-yellow: #f3c623;
    --bean-blue: #2a9ad6;
    --bean-green: #3aa84a;
    --bean-purple: #8a4fa6;
  }
  * { margin: 0; padding: 0; box-sizing: border-box; }
  html, body {
    width: 1200px;
    height: 2420px;
    overflow: hidden;
    background: var(--paper);
  }
  .flyer {
    position: relative;
    width: 1200px;
    height: 2420px;
    overflow: hidden;
    background: var(--paper);
    font-family: "Fredoka", "Arial Rounded MT Bold", sans-serif;
    color: var(--ink);
  }
  .flyer-shapes {
    position: absolute;
    inset: 0;
    width: 1200px;
    height: 2420px;
  }
  .brand-name {
    position: absolute;
    left: 130px;
    top: 352px;
    width: 1010px;
    font-weight: 600;
    font-size: 128px;
    line-height: 1;
    letter-spacing: 2px;
    text-transform: uppercase;
    color: var(--ink);
    white-space: nowrap;
  }
  .challenge {
    position: absolute;
    left: 0;
    top: 648px;
    width: 1200px;
    font-weight: 500;
    font-size: 76px;
    line-height: 93px;
    color: var(--ink);
  }
  .challenge span { display: block; white-space: nowrap; }
  .challenge .line-1 { padding-left: 172px; }
  .challenge .line-2 { padding-left: 214px; }
  .challenge .line-3 { padding-left: 255px; word-spacing: 22px; }
  .prize {
    position: absolute;
    left: 560px;
    top: 1070px;
    width: 500px;
    text-align: center;
    font-family: "Black Ops One", "Impact", sans-serif;
    font-size: 150px;
    line-height: 1;
    letter-spacing: 4px;
    color: #f4efef;
    text-shadow: 4px 5px 6px rgba(90, 0, 0, 0.45);
  }
  .platform-note {
    position: absolute;
    right: 168px;
    top: 2170px;
    font-weight: 500;
    font-size: 58px;
    line-height: 79px;
    color: var(--ink);
    text-align: right;
  }
  .platform-note span { display: block; white-space: nowrap; }
  .platform-note .line-1 { margin-right: -22px; }
</style>
</head>
<body>
<main class="flyer">
  <svg class="flyer-shapes" viewBox="0 0 1200 2420" xmlns="http://www.w3.org/2000/svg" aria-hidden="false">
    <defs>
      <radialGradient id="prize-glow" cx="0.5" cy="0.5" r="0.5">
        <stop offset="0" stop-color="#ffd9da" stop-opacity="0.95"/>
        <stop offset="0.5" stop-color="#f6888c" stop-opacity="0.6"/>
        <stop offset="1" stop-color="#ed2e35" stop-opacity="0"/>
      </radialGradient>
      <linearGradient id="bean-tones" x1="0" y1="0" x2="1" y2="1">
        <stop offset="0" stop-color="#4aa7d8"/>
        <stop offset="0.2" stop-color="#e8463a"/>
        <stop offset="0.4" stop-color="#f3c623"/>
        <stop offset="0.55" stop-color="#3aa84a"/>
        <stop offset="0.72" stop-color="#ef7aa0"/>
        <stop offset="0.86" stop-color="#8a4fa6"/>
        <stop offset="1" stop-color="#f08a2a"/>
      </linearGradient>
    </defs>

    <!-- red sweep -->
    <path class="red-sweep" fill="var(--red)"
          d="M150 0 H1200 V2140 H0 V150 C50 90 100 40 150 0 Z"/>

    <!-- white wave under the brand name -->
    <path class="white-wave" fill="var(--paper)"
          d="M1200 240 C1090 400 990 510 900 565 C1010 560 1110 560 1200 570 Z"/>

    <!-- plain brand square -->
    <rect class="brand-square" x="756" y="36" width="320" height="262" rx="6"
          fill="var(--red)" stroke="var(--paper)" stroke-width="4"/>

    <!-- glow behind prize -->
    <ellipse class="prize-glow" cx="805" cy="1150" rx="330" ry="190" fill="url(#prize-glow)"/>

    <!-- jelly bean photograph area -->
    <path class="bean-photo" role="img" aria-label="Photograph of a pile of colourful jelly beans"
          fill="url(#bean-tones)"
          d="M0 682 C197 789 329 921 427 1052 C625 1348 904 1480 1200 1545 V2140 H66 Q0 2140 0 2074 Z"/>

    <!-- pale footer band -->
    <rect class="footer-band" x="0" y="2140" width="1200" height="280" fill="var(--blush)"/>
  </svg>

  <div class="brand-name">Velvet Orbit</div>

  <p class="challenge">
    <span class="line-1">Take the jelly bean challange</span>
    <span class="line-2">at the velvet orbit table in</span>
    <span class="line-3">the exibit space and win a</span>
  </p>

  <div class="prize">DRONE</div>

  <p class="platform-note">
    <span class="line-1">Find out more about our qTallon</span>
    <span class="line-2">Web services platform for</span>
    <span class="line-3">Financial Models</span>
  </p>
</main>
</body>
</html>
```